Sophrologist needs a cool signage at door entrance

I need signage for dr in sophrology based in Belgium (french speaking). The signed should capture the name the "Mireille Vantoorn" - "Naturopathe-Sophrologue-Reiki" and a catchphrase = (Healthy way of life)
« Fais du bien à ton corps, pour que ton âme ait envie d’y rester »
Requirements
Must have
- Hey,
Thats the instagram account for some inspiration www.instagram.com/mireille_serene_wellbeing
Light colors, green, blue
Healthy way of life
Size is 45cm wide on 30 cm high
The signage will be placed in front off woof pannel

```html
<!DOCTYPE html>
<html lang="fr">
<head>
<meta charset="utf-8">
<title>Mireille Vantoorn – Naturopathe-Sophrologue-Reiki</title>
<link rel="stylesheet" href="https://fonts.googleapis.com/css2?family=Oswald:wght@300&family=Marcellus&family=Great+Vibes&display=swap">
<style>
  :root {
    --navy: #1c4188;
    --leaf: #7ac143;
    --leaf-dark: #4f9a2e;
    --leaf-light: #a6d66d;
    --ink-green: #1f3616;
    --wood-light: #fbfbf9;
    --wood-shade: #ecebe6;
    --white: #ffffff;
  }
  * { margin: 0; padding: 0; box-sizing: border-box; }
  html, body {
    width: 1200px;
    height: 825px;
    overflow: hidden;
    background: var(--white);
  }
  .sign {
    position: relative;
    width: 1200px;
    height: 825px;
    overflow: hidden;
  }
  .wood-panel {
    position: absolute;
    inset: 0;
    background: linear-gradient(180deg, var(--wood-light) 0%, var(--wood-shade) 50%, var(--wood-light) 100%);
  }
  .frame, .foliage {
    position: absolute;
    inset: 0;
  }
  .owner-name {
    position: absolute;
    left: 0;
    width: 1200px;
    top: 80px;
    text-align: center;
    font-family: "Oswald", "Arial Narrow", sans-serif;
    font-weight: 300;
    font-size: 112px;
    line-height: 1;
    letter-spacing: 3px;
    color: var(--navy);
  }
  .practice-band {
    position: absolute;
    left: 125px;
    top: 227px;
    width: 949px;
    height: 83px;
    border-radius: 42px;
    background: var(--leaf);
    display: flex;
    align-items: center;
    justify-content: center;
    font-family: "Marcellus", "Optima", serif;
    font-size: 44px;
    letter-spacing: 1px;
    color: var(--white);
    padding-top: 4px;
  }
  .motto {
    position: absolute;
    left: 141px;
    width: 915px;
    top: 372px;
    text-align: center;
    font-family: "Great Vibes", cursive;
    font-size: 142px;
    line-height: 1;
    white-space: nowrap;
    color: var(--navy);
  }
  .tagline {
    position: absolute;
    left: 0;
    width: 1200px;
    top: 604px;
    text-align: center;
    font-family: "Marcellus", "Optima", serif;
    font-size: 30px;
    line-height: 41px;
    color: var(--ink-green);
  }
</style>
</head>
<body>
<main class="sign">
  <div class="wood-panel" role="img" aria-label="Fond en planches de bois blanchies"></div>

  <svg class="frame" width="1200" height="825" viewBox="0 0 1200 825" aria-hidden="true">
    <polyline points="386,791 29,791 29,32 1170,32 1170,433" fill="none" stroke="var(--navy)" stroke-width="4"/>
  </svg>

  <svg class="foliage" width="1200" height="825" viewBox="0 0 1200 825" role="img" aria-label="Branches de feuilles vertes en bordure du panneau">
    <defs>
      <linearGradient id="leaf-fill" x1="0" y1="0" x2="0" y2="1">
        <stop offset="0" stop-color="var(--leaf-light)"/>
        <stop offset="1" stop-color="var(--leaf-dark)"/>
      </linearGradient>
    </defs>
    <path d="M1176 0 H1200 V825 H0 V730 C40 720 80 745 120 748 C200 740 260 752 320 745 C400 740 450 755 520 750 C580 740 640 748 690 740 C770 730 860 660 900 600 C960 560 1000 480 1040 450 C1090 440 1130 430 1165 410 C1178 300 1170 100 1176 0 Z" fill="url(#leaf-fill)" opacity="0.85"/>
  </svg>

  <h1 class="owner-name">MIREILLE VANTOORN</h1>
  <p class="practice-band">NATUROPATHE-SOPHROLOGUE-REIKI</p>
  <p class="motto">Healthy way of life</p>
  <p class="tagline">Fais du bien à ton corps,<br>pour que ton âme ait envie d’y rester</p>
</main>
</body>
</html>
```